Creatives for Lead Generation Campaign

NestlingHome provides expert advice and informative articles on everything from pregnancy symptoms to baby milestones and beyond. Millions of members are in the know thanks to continually expanding offerings including interactive tools, like our gender predictor; personalized content, like our week by week development newsletters; and member rewards programs.

We're looking for new, high quality, email creative and banners for a lead generation campaign for our site. The campaign is for a free membership to our site, and access to offers for Free Baby Stuff. I've attached our current creatives, but we are looking for something fresh and different from these. We would like to highlight some of the features of our site, without losing focus on what effectively drives registrations, which is the free baby stuff. The larger email creative will have more room for feature explanation and text, while the smaller banner sizes will need to be more singularly focused. the main goal here is compelling! A design that's so attention grabbing that our target audience can't help but to click on it and immediately sign up.

Landing Page for Creatives:
http://www.nestlinghome.example/lp/nh550/ or http://www.nestlinghome.example/lp/nh269/
You can also review our organic registration form for additional ideas/features : http://www.nestlinghome.example/register/

Sizes :
Please create a 160x600, a 300x250 and the email creative (550px width) for review during the contest
Once selected as a winner, please generate the following sizes as well as your PSD files
• Banner: 468 x 60
• Leaderboard: 728 x 90
• Square: 250 x 250
• Small square: 200 x 200
• Large rectangle: 336 x 280
• Inline rectangle: 300 x 250
• Skyscraper: 120 x 600
• Wide skyscraper: 160 x 600
• Half-page: 300 x 600

If needed, you may use photos from any photo stock site (we will buy them) - not a problem

If you have any ideas you'd like to bounce off of me, feel free to reach out. I'm available and looking forward to working with you. Thanks!

Target Market(s)

Mothers and soon-to-be-mothers – Please consider what would compel our target audience

Industry/Entity Type

Baby

Requirements
Must have
• Guidelines:
Cannot use any images of branded products
Creative should utilize a strong call to action
Be short, concise and to the point
Talk about benefits, not features
Keep the main message and its CTA above the fold
Use actionable language in each CTA
For bonus points, feel free to animate the banners – Flash or animated GIF
MUST comply with PromoLinker policy - http://help.quorvex.example/promolinkerpolicy/bin/answer.py?hl=en&answer=482731
Nice to have
• Example Messaging (feel free to come up with something new as well):
Free Baby Stuff – Limited Time
Hurry These Will Go Fast! Join now to start receiving free stuff for baby straight to your home.
Win Free Diapers for a Year!
Premium Baby Samples. Brands you Trust! Supplies are limited. Act now!
Hurry These Will Go Fast! Top Brands Are Giving Away Free Baby Samples. Get Your Free Samples Now. Register Now!
Join now to start receiving free stuff for baby straight to your home.
Looking For Baby Coupons?
Want FREE Baby Samples?
Get FREE Baby Stuff
Hurry Before It's Too Late! Join today and start receiving free baby stuff to your home.
Are You Expecting?
Hurry These Will Go Fast! Get Your Free Samples Now!
100% Free Baby Stuff - Here's A Quick Way To Get Free Baby Samples In Less Than 5 Minutes
Hundreds of Baby Coupons - Choose the Coupons That You Want
Looking For Baby Coupons? - Sign Up Today for Your Coupons

```html
<!DOCTYPE html>
<html lang="en">
<head>
<meta charset="utf-8">
<title>NestlingHome Free Baby Stuff Leaderboard</title>
<link href="https://fonts.googleapis.com/css2?family=Arimo:wght@400;700&display=swap" rel="stylesheet">
<style>
  :root {
    --brand-green: #6dbb3c;
    --brand-green-dark: #4f9a24;
    --brand-blue: #1f63ad;
    --band-deep: #0d2f6e;
    --band-mid: #1c4f96;
    --band-light: #2d6bb5;
    --paper: #ffffff;
    --frame: #c9d3e0;
  }
  html, body {
    margin: 0;
    padding: 0;
    overflow: hidden;
    background: var(--paper);
  }
  .leaderboard {
    position: relative;
    width: 1200px;
    height: 148px;
    background: var(--paper);
    box-sizing: border-box;
    border: 1px solid var(--frame);
    overflow: hidden;
    font-family: "Arimo", Arial, sans-serif;
  }
  .brand {
    position: absolute;
    left: 0;
    top: 0;
    width: 247px;
    height: 146px;
    display: flex;
    flex-direction: column;
    align-items: center;
    justify-content: center;
    gap: 12px;
  }
  .brand-dot {
    width: 62px;
    height: 62px;
    border-radius: 50%;
    background: var(--brand-green);
  }
  .brand-name {
    font-size: 17px;
    font-weight: 700;
    letter-spacing: 0.5px;
    color: var(--brand-blue);
  }
  .band {
    position: absolute;
    left: 247px;
    top: 4px;
    width: 717px;
    height: 140px;
    background: linear-gradient(90deg, var(--band-deep) 0%, var(--band-mid) 45%, var(--band-light) 100%);
  }
  .headline {
    position: absolute;
    left: 36px;
    top: 14px;
    margin: 0;
    font-size: 20px;
    font-weight: 700;
    letter-spacing: 2.4px;
    color: var(--brand-green);
    white-space: nowrap;
  }
  .subline {
    position: absolute;
    left: 36px;
    top: 48px;
    margin: 0;
    font-size: 15px;
    font-weight: 400;
    color: var(--paper);
    white-space: nowrap;
  }
  .cta {
    position: absolute;
    left: 36px;
    top: 82px;
    height: 40px;
    padding: 0 22px;
    display: flex;
    align-items: center;
    border-radius: 20px;
    background: var(--brand-green);
    box-shadow: inset 0 -3px 0 var(--brand-green-dark);
    color: var(--paper);
    font-size: 16px;
    font-weight: 700;
    letter-spacing: 1px;
    text-decoration: none;
    white-space: nowrap;
  }
  .photo {
    position: absolute;
  }
  .photo-bubbles {
    left: 380px;
    top: 40px;
    width: 120px;
    height: 100px;
    background: radial-gradient(ellipse at 50% 45%, #e9c6a6 0%, #8aa3c8 55%, rgba(45,107,181,0) 78%);
  }
  .photo-play {
    left: 520px;
    top: 46px;
    width: 173px;
    height: 94px;
    background: radial-gradient(ellipse at 50% 50%, #e4b994 0%, #c7504a 35%, #6b8fc4 62%, rgba(45,107,181,0) 82%);
  }
  .photo-feeding {
    left: 964px;
    top: 0;
    width: 236px;
    height: 146px;
    background: linear-gradient(120deg, #f3e4d8 0%, #f7efe9 40%, #ffffff 70%, #f1ede9 100%);
  }
</style>
</head>
<body>
  <div class="leaderboard">
    <div class="brand">
      <span class="brand-dot"></span>
      <span class="brand-name">NESTLINGHOME.COM</span>
    </div>
    <div class="band">
      <h1 class="headline">GET FREE BABY STUFF – LIMITED TIME!</h1>
      <p class="subline">Free samples sent straight to your home.</p>
      <a class="cta" href="http://www.nestlinghome.example/lp/nh550/">SIGN UP FREE NOW ›</a>
      <div class="photo photo-bubbles" role="img" aria-label="Young child blowing soap bubbles"></div>
      <div class="photo photo-play" role="img" aria-label="Two toddlers playing with colourful toys"></div>
    </div>
    <div class="photo photo-feeding" role="img" aria-label="Baby being fed from a bottle by a parent's hand"></div>
  </div>
</body>
</html>
```